Vehicle Signage Design for a Renovation Company

We're a renovation company specialising in Home Renovations. The final design should communicate trust, credibility, and confidence. We need vehicle signage designed for our company utes (see attachment) / for our grey ute with the canopy/ and white use withou the canopyI've also attached our existing designs for the current vehicles (van and hatch back) to give you an idea of what we're after.In terms of content, there isn't much requirement for this due to the limited space on the ute - but happy to hear ideas on this.We've tried designing it ourselves - see attachment, but not happy with the result, would like more variations and ideas.Check out our website www.brightwallbuilders.co.nz for ideas on our branding/ style.

Target Market(s)

Home Owners

Industry/Entity Type

Residential Construction

Font styles to use
Sans Serif

Colors
3276b5
0355a3
33a6d7
3aa7d7
ffffff

Requirements
Must have
• Logo, Call to Action (website and number), Headline
Nice to have
• Strong sharp lines, a clean/sleek look
• It would be nice to have our offer on there (free design plans) / but we know space is limited

```html
<!DOCTYPE html>
<html lang="en">
<head>
<meta charset="utf-8">
<title>Brightwall Builders – Ute Wrap Layout</title>
<link href="https://fonts.googleapis.com/css2?family=Exo+2:wght@400;500;600;700&display=swap" rel="stylesheet">
<style>
  :root {
    --navy: #1f2a6b;
    --blue: #2f62b0;
    --green: #5cb135;
    --green-text: #6cc24a;
    --white: #ffffff;
    --cutline: #e0262b;
    --ring: #e39a2d;
  }
  html, body {
    margin: 0;
    padding: 0;
    width: 1200px;
    height: 886px;
    overflow: hidden;
    background: var(--white);
  }
  .canvas {
    position: relative;
    width: 1200px;
    height: 886px;
  }
  .wrap-layout {
    position: absolute;
    left: 20px;
    top: 265px;
    width: 1160px;
    height: 352px;
  }
  .wrap-layout text {
    font-family: "Exo 2", sans-serif;
    fill: var(--white);
  }
  .cutline { fill: none; stroke: var(--cutline); stroke-width: 1.3; }
  .brand-name { fill: var(--navy) !important; font-weight: 700; font-size: 36px; }
  .headline-light { font-size: 37px; font-weight: 400; }
  .headline-bold { font-size: 48px; font-weight: 700; }
  .offer-band { fill: var(--green); }
  .offer-text { font-size: 15.5px; font-weight: 500; }
  .trust-text { font-size: 14.5px; font-weight: 600; }
  .cta-kicker { font-size: 13px; font-weight: 400; }
  .cta-phone { fill: var(--green-text) !important; font-size: 35px; font-weight: 700; }
  .cta-web { font-size: 14.5px; font-weight: 500; }
  .side-offer { font-size: 15.5px; font-weight: 500; }
  .side-offer-strong { font-weight: 700; }
  .photo-ring { stroke: var(--ring); stroke-width: 1.5; }
</style>
</head>
<body>
<div class="canvas">
  <svg class="wrap-layout" viewBox="30 615 1450 440" xmlns="http://www.w3.org/2000/svg">
    <defs>
      <linearGradient id="wrapBlue" x1="0" y1="0" x2="1" y2="0">
        <stop offset="0" stop-color="#1f2a6b"/>
        <stop offset="0.5" stop-color="#243d8a"/>
        <stop offset="1" stop-color="#3068b5"/>
      </linearGradient>
      <linearGradient id="kitchenTones" x1="0" y1="0" x2="1" y2="1">
        <stop offset="0" stop-color="#b9c3c9"/>
        <stop offset="0.55" stop-color="#8a8178"/>
        <stop offset="1" stop-color="#4b4a4c"/>
      </linearGradient>
      <linearGradient id="bathroomTones" x1="0" y1="0" x2="1" y2="1">
        <stop offset="0" stop-color="#c7a07a"/>
        <stop offset="1" stop-color="#d9d9d6"/>
      </linearGradient>
    </defs>

    <!-- front lower panel -->
    <path class="wrap-panel" fill="url(#wrapBlue)" d="M45,945 L162,922 L140,1030 L45,985 Z"/>
    <!-- main side panel -->
    <path class="wrap-panel" fill="url(#wrapBlue)" d="M398,868 Q600,818 1000,792 Q1300,785 1457,800 L1460,905 L1470,925 L1300,1002 L1290,900 Q1270,862 1165,860 Q1080,864 1052,940 L1040,1024 L420,1040 Z"/>

    <!-- vehicle cutline -->
    <path class="cutline" d="M45,985 L48,915 L95,905 L138,873 L158,835 L86,832 L90,815 Q100,792 160,782 L420,762 L578,650 L600,645 L1000,625 L1025,640 L1045,770 L1455,770 L1462,810 L1460,905 L1470,925 L1300,1002 L1290,900 Q1270,862 1165,860 Q1080,864 1052,940 L1040,1024 L420,1040 L400,900 Q380,880 290,882 Q200,885 168,910 L140,1030 Z"/>
    <path class="cutline" d="M470,792 L572,698 Q592,650 640,650 L768,648 L752,780 Z"/>
    <rect class="cutline" x="800" y="645" width="182" height="130" rx="16"/>
    <rect class="cutline" x="695" y="826" width="60" height="12" rx="6"/>
    <rect class="cutline" x="940" y="816" width="62" height="14" rx="7"/>

    <!-- photo circles -->
    <circle class="photo-ring" cx="890" cy="872" r="103" fill="url(#kitchenTones)" role="img" aria-label="Photo of a renovated modern kitchen with timber island bench"/>
    <circle class="photo-ring" cx="772" cy="972" r="55" fill="url(#bathroomTones)" role="img" aria-label="Photo of a renovated bathroom with freestanding bath"/>

    <!-- brand -->
    <text class="brand-name" x="172" y="846">Brightwall Builders</text>

    <!-- headline -->
    <text class="headline-light" x="428" y="900">THINKING ABOUT</text>
    <text class="headline-bold" x="426" y="941">RENOVATING</text>
    <text class="headline-light" x="428" y="975">YOUR HOME?</text>

    <!-- offer band -->
    <rect class="offer-band" x="410" y="983" width="312" height="28"/>
    <text class="offer-text" x="427" y="1003">Get your free design plans (worth $2,500)</text>

    <!-- trust band -->
    <rect class="offer-band" x="892" y="982" width="148" height="19"/>
    <text class="trust-text" x="970" y="978" text-anchor="middle">Trusted</text>
    <text class="trust-text" x="970" y="997" text-anchor="middle">Home Renovation</text>
    <text class="trust-text" x="970" y="1014" text-anchor="middle">Experts</text>

    <!-- call to action -->
    <text class="cta-kicker" x="1028" y="813">secure your spot now</text>
    <text class="cta-phone" x="1027" y="846">0800 555 012</text>
    <text class="cta-web" x="1028" y="862">www.brightwallbuilders.co.nz</text>

    <!-- side offer -->
    <text class="side-offer" x="1354" y="880" text-anchor="middle"><tspan class="side-offer-strong">Book a</tspan></text>
    <text class="side-offer" x="1354" y="898" text-anchor="middle"><tspan class="side-offer-strong">free design</tspan></text>
    <text class="side-offer" x="1354" y="915" text-anchor="middle">to build</text>
    <text class="side-offer" x="1354" y="932" text-anchor="middle">consultation</text>
  </svg>
</div>
</body>
</html>
```